Business Card Design for new consultancy company

Name of Company: Orbit Lanternway
Nature of Business: Digital Business Consultancy
Specialises in Digital Media Strategy, Digital Business Model Transformation, Over-The-Top (OTT) Development, Web Business Development, Digital Marketing, Web and App Product Development, Design and Innovation

Website: http://www.orbit-lanternway.example

Designs can be of any colour or any number of colours, objective is to give the impression we are a digital trend setter, creative and impactful.

Also please suggest a logo to complement the name and business card.

Target Market(s)

Media Companies, Telcos, Enterprises

Industry/Entity Type

Business

Contact Information for Business Card

Standard business card size. OK with to play with small variations like corners for impact/impression.

Font styles to use
Serif
Sans Serif

Requirements
Must have
• Clarity, Impact, Creativity
Nice to have
• Design should encapsulate professionalism, expertise, yet trend-setting and vibrant for digital consultancy
Should not have
• Messy layout, too gaudy colours or design

```html
<!DOCTYPE html>
<html lang="en">
<head>
<meta charset="utf-8">
<title>Orbit Lanternway — Business Card</title>
<link rel="stylesheet" href="https://fonts.googleapis.com/css2?family=Open+Sans:wght@300;400;600&display=swap">
<style>
  :root {
    --backdrop: #2b2724;
    --card: #161616;
    --card-edge: #232323;
    --brand-grey: #c9c9c9;
    --text-light: #e6e6e6;
    --text-muted: #b4b4b4;
    --divider: #3a3a3a;
  }
  * { margin: 0; padding: 0; box-sizing: border-box; }
  html, body {
    width: 1200px; height: 844px; overflow: hidden;
    background: var(--backdrop);
    font-family: "Open Sans", Arial, sans-serif;
  }
  .stage {
    position: relative; width: 1200px; height: 844px;
    display: flex; align-items: center; justify-content: center; gap: 40px;
  }
  .card {
    position: relative; width: 520px; height: 300px;
    background: linear-gradient(150deg, #1d1d1d 0%, var(--card) 60%, #111 100%);
    border: 1px solid var(--card-edge);
    box-shadow: 0 10px 30px rgba(0,0,0,0.45);
  }
  /* Front: contact side */
  .card-front .brand {
    position: absolute; left: 0; top: 0; width: 250px; height: 300px;
    display: flex; flex-direction: column; align-items: center; justify-content: center; gap: 14px;
  }
  .brand-dot {
    width: 46px; height: 46px; border-radius: 50%;
    border: 3px solid var(--brand-grey);
  }
  .brand-name {
    font-weight: 300; color: var(--brand-grey);
    font-size: 19px; letter-spacing: 0.5px; text-transform: uppercase; white-space: nowrap;
  }
  .card-front .divider {
    position: absolute; left: 262px; top: 40px; width: 1px; height: 220px;
    background: var(--divider);
  }
  .contact {
    position: absolute; left: 284px; top: 50px; color: var(--text-muted);
  }
  .person-name { font-size: 22px; font-weight: 600; color: var(--text-light); line-height: 1.1; }
  .person-role { font-size: 11px; color: var(--text-light); margin-top: 3px; }
  .contact-lines { margin-top: 22px; font-size: 12px; line-height: 1.45; }
  .address { margin-top: 14px; font-size: 12.5px; line-height: 1.4; color: var(--text-light); }
  /* Back: brand side */
  .card-back {
    display: flex; flex-direction: column; align-items: center; justify-content: center; gap: 18px;
  }
  .card-back .brand-dot { width: 60px; height: 60px; border-color: #7c7c7c; }
  .card-back .brand-name { font-size: 24px; color: #7c7c7c; }
</style>
</head>
<body>
  <main class="stage">
    <section class="card card-front" aria-label="Business card, contact side">
      <div class="brand">
        <span class="brand-dot"></span>
        <span class="brand-name">Orbit Lanternway</span>
      </div>
      <div class="divider"></div>
      <div class="contact">
        <p class="person-name">Mara Quillfield</p>
        <p class="person-role">Managing Director</p>
        <div class="contact-lines">
          <p>T: 044-555 010 246</p>
          <p>E: info@orbit-lanternway.example</p>
          <p>W: www.orbit-lanternway.example</p>
        </div>
        <div class="address">
          <p>48 Lantern Row, Suite 5</p>
          <p>Northvale, 204816.</p>
        </div>
      </div>
    </section>
    <section class="card card-back" aria-label="Business card, brand side">
      <span class="brand-dot"></span>
      <span class="brand-name">Orbit Lanternway</span>
    </section>
  </main>
</body>
</html>
```